Cover for "ROOTED! The skill and rhythm of guiding teams through calm and delight"

My first book for a global audience of modern performance leaders needs its cover!
I am an international executive coach and I've developed a new approach to replace classic Performance Management with a natural, sustainable approach fit for human beings :) My first book is about this approach and serves two purposes: helping leaders and sparking their curiosity to learn more, and positioning myself as a thought leader in the field.
The book is built on personal experience; it is both professional and personal ("From me to You"), and I'd like to position it beyond classic categorisation.
Its cover should communicate humanness, naturalness, ease and joy, within an unmistakably business-y context. I would like to see designs that use the color yellow (but not sure it communicates the right things).
Updates

Target Market(s)

Leaders who aspire to have a positive impact and deliver results in a meaningful way

Industry/Entity Type

Consulting & Executive Coaching - Trusted Advisor

Font styles to use
Other font styles liked:
• Helvetica Neue

Colors
0094D4
00A9DD
6FCCEA
C7EBF8
E9F6FB
FFC000
F8CF3A
FAE287
FDF2CF
FEFAEE
EE7325
F08F49
F5BC92
FAE3D3
FDF4ED

Requirements
Must have
• A both-and feeling to it (see description), e.g., masculine AND feminine, business AND humanness. Power with, not power over...
Should not have
• Too much "bling" - no classic status symbol business success language

```html
<!DOCTYPE html>
<html lang="en">
<head>
<meta charset="utf-8">
<title>ROOTED! — Book Cover</title>
<link href="https://fonts.googleapis.com/css2?family=Arimo:wght@700&display=swap" rel="stylesheet">
<style>
  :root {
    --page-bg: #ffffff;
    --cover-yellow: #fdc40f;
    --cover-yellow-deep: #f7bd08;
    --ink: #2b2b2b;
  }
  html, body {
    margin: 0;
    padding: 0;
    width: 1200px;
    height: 1200px;
    overflow: hidden;
    background: var(--page-bg);
  }
  .cover {
    position: absolute;
    left: 222px;
    top: 50px;
    width: 756px;
    height: 1100px;
    overflow: hidden;
    background: linear-gradient(180deg, var(--cover-yellow) 0%, var(--cover-yellow-deep) 100%);
    font-family: "Arimo", "Helvetica Neue", Arial, sans-serif;
    font-weight: 700;
    color: var(--ink);
  }
  .cover-art {
    position: absolute;
    inset: 0;
    width: 100%;
    height: 100%;
  }
  .cover-art .shadow-field { fill: var(--ink); }
  .cover-art .hero-placeholder { fill: url(#heroTone); }
  .title {
    position: absolute;
    left: 0;
    right: 0;
    top: 77px;
    margin: 0;
    text-align: center;
    font-size: 148px;
    line-height: 1;
    letter-spacing: -4px;
    font-weight: 700;
  }
  .subtitle {
    position: absolute;
    left: 0;
    right: 0;
    top: 260px;
    margin: 0;
    text-align: center;
    font-size: 32px;
    line-height: 46px;
    letter-spacing: 0.2px;
    font-weight: 700;
    text-transform: uppercase;
  }
  .author {
    position: absolute;
    left: 0;
    right: 0;
    top: 1019px;
    margin: 0;
    text-align: center;
    font-size: 42px;
    line-height: 1;
    letter-spacing: 4px;
    color: var(--cover-yellow);
    text-transform: uppercase;
  }
</style>
</head>
<body>
  <main class="cover">
    <svg class="cover-art" viewBox="0 0 955 1390" preserveAspectRatio="none" aria-hidden="true">
      <path class="shadow-field" d="M0,963 C220,800 470,620 955,483 L955,1390 L0,1390 Z"/>
    </svg>
    <svg class="cover-art" viewBox="0 0 955 1390" preserveAspectRatio="none" role="img" aria-label="Illustration: silhouette of a person with a raised fist on a hilltop before a rising sun">
      <defs>
        <linearGradient id="heroTone" x1="0" y1="0" x2="0" y2="1">
          <stop offset="0%" stop-color="#f7bd08"/>
          <stop offset="100%" stop-color="#6b5a1e"/>
        </linearGradient>
      </defs>
      <rect class="hero-placeholder" x="306" y="860" width="345" height="338"/>
    </svg>
    <h1 class="title">ROOTED!</h1>
    <p class="subtitle">The skill and rhythm of guiding<br>teams through calm and delight</p>
    <p class="author">Author Name</p>
  </main>
</body>
</html>
```